KB Rubbish Removal Business Card

Hey,
I need a double sided business card designed for a rubbish removal business based in Australia. Logo is already chosen, similar colours preferred for both sides of the business card.

Details to include:

Front:

KB Rubbish Removal
Darren Holloway
Managing Director
Mobile: 0471 902 146
Email: darren@kbrubbishremoval.com.au
Website: kbrubbishremoval.com.au

Rear:

How did we do?
kbrubbishremoval.com.au/review

```html
<!DOCTYPE html>
<html lang="en">
<head>
<meta charset="utf-8">
<title>KB Rubbish Removal Business Card</title>
<link rel="stylesheet" href="https://fonts.googleapis.com/css2?family=Montserrat:wght@700&family=Open+Sans:wght@400;600&display=swap">
<style>
  :root {
    --bg: #2a2b2d;
    --white: #ffffff;
    --green-deep: #0f6b32;
    --green-mid: #1b8a3e;
    --green-bright: #2fae4c;
    --green-light: #7cc24a;
    --green-shade: #17753a;
    --ink: #333333;
  }
  * { box-sizing: border-box; margin: 0; padding: 0; }
  html, body { width: 1200px; height: 900px; overflow: hidden; }
  body {
    background: var(--bg);
    display: flex;
    flex-direction: column;
    align-items: center;
    justify-content: center;
    gap: 44px;
  }
  .card {
    position: relative;
    width: 680px;
    height: 388px;
    border-radius: 22px;
    overflow: hidden;
  }

  /* Front */
  .card--front {
    background: var(--white);
    padding: 58px 60px 0 110px;
  }
  .brand {
    display: flex;
    align-items: center;
    gap: 14px;
    margin-left: 150px;
  }
  .brand__dot {
    width: 40px;
    height: 40px;
    border-radius: 50%;
    background: var(--green-bright);
    flex: none;
  }
  .brand__name {
    font-family: "Open Sans", sans-serif;
    font-weight: 600;
    font-size: 26px;
    color: var(--green-deep);
    line-height: 1.2;
    white-space: nowrap;
  }
  .person { margin-top: 48px; }
  .person__name {
    font-family: "Montserrat", sans-serif;
    font-weight: 700;
    font-size: 25px;
    color: var(--green-mid);
    text-transform: uppercase;
    letter-spacing: 0.5px;
  }
  .person__role {
    font-family: "Open Sans", sans-serif;
    font-size: 16px;
    color: var(--green-light);
    margin-top: 2px;
    margin-left: 40px;
  }
  .divider {
    display: block;
    margin: 10px 0 6px -40px;
  }
  .contacts {
    list-style: none;
    font-family: "Open Sans", sans-serif;
    font-size: 17px;
    color: var(--ink);
    line-height: 1.45;
  }
  .contacts .phone { margin-left: 120px; }

  /* Back */
  .card--back {
    background: linear-gradient(120deg, var(--green-deep) 0%, var(--green-mid) 55%, var(--green-bright) 100%);
    display: flex;
    flex-direction: column;
    align-items: center;
    justify-content: center;
  }
  .back-brand {
    display: flex;
    align-items: center;
    gap: 16px;
  }
  .back-brand__dot {
    width: 52px;
    height: 52px;
    border-radius: 50%;
    background: var(--green-shade);
  }
  .back-brand__name {
    font-family: "Open Sans", sans-serif;
    font-weight: 600;
    font-size: 34px;
    color: var(--green-shade);
    line-height: 1.2;
    white-space: nowrap;
  }
  .review {
    margin-top: 52px;
    text-align: center;
    font-family: "Open Sans", sans-serif;
    color: var(--white);
    font-size: 20px;
    line-height: 1.4;
  }
</style>
</head>
<body>

<section class="card card--front" aria-label="Business card front">
  <div class="brand">
    <span class="brand__dot"></span>
    <span class="brand__name">KB Rubbish Removal</span>
  </div>

  <div class="person">
    <h1 class="person__name">Darren Holloway</h1>
    <p class="person__role">Managing Director</p>
  </div>

  <svg class="divider" width="360" height="34" viewBox="0 0 360 34" aria-hidden="true">
    <g fill="none" stroke="#1b8a3e" stroke-width="1.5">
      <line x1="0" y1="17" x2="100" y2="17"/>
      <line x1="126" y1="17" x2="150" y2="17"/>
      <line x1="176" y1="17" x2="200" y2="17"/>
      <line x1="226" y1="17" x2="360" y2="17"/>
      <circle cx="113" cy="17" r="12"/>
      <circle cx="163" cy="17" r="12"/>
      <circle cx="213" cy="17" r="12"/>
    </g>
    <path d="M108 11c1-1 2-1 2.5 0l1 2c.4.8 0 1.3-.6 1.8 .8 1.6 1.8 2.6 3.3 3.3.5-.6 1-1 1.8-.6l2 1c1 .5 1 1.5 0 2.5-2 2-9-4-10-10z" fill="#1b8a3e"/>
    <rect x="156" y="12" width="14" height="10" rx="1" fill="#1b8a3e"/>
    <path d="M156.5 12.5l6.5 5 6.5-5" fill="none" stroke="#fff" stroke-width="1.2"/>
    <g fill="none" stroke="#1b8a3e" stroke-width="1.3">
      <circle cx="213" cy="17" r="6.5"/>
      <ellipse cx="213" cy="17" rx="3" ry="6.5"/>
      <line x1="206.5" y1="17" x2="219.5" y2="17"/>
    </g>
  </svg>

  <ul class="contacts">
    <li class="phone">0471 902 146</li>
    <li>darren@kbrubbishremoval.com.au</li>
    <li>www.kbrubbishremoval.com.au</li>
  </ul>
</section>

<section class="card card--back" aria-label="Business card back">
  <div class="back-brand">
    <span class="back-brand__dot"></span>
    <span class="back-brand__name">KB Rubbish Removal</span>
  </div>
  <p class="review">How did we do?<br>www.kbrubbishremoval.com.au/review</p>
</section>

</body>
</html>
```